依頼概要
ハガキを送る際に住所と会社名、似顔絵などをいれたスタンプの作成をお願いしたいと思います。
名刺交換をした方やお世話になっている方にお礼状を書く際に、今まで住所を手書きで書いていたのですが、量が増えると大変なので、スタンプを作成したいと思います。
しかし、ただのスタンプだと味気ないので、似顔絵入りを作成したいと思います。

サイズは、30×80mm(横×縦)
https://www.morinoki-insho.example/item/kaku_030x080.html
上記のサイトから注文したいと思います。

1、住所
2、会社名
3、代表取締役と名前
この3点と顔のイラストが入った物を組み合わせていただければと思います。
身体は、スーツっぽくしてください。
これらの情報は、お願いする人が決定したらお送りします。

2名分お願いします。もう一人は、役職なしです。
納入方法は、
PDFとAiでお願いします。
宜しくお願いいたします。

色々なタイプの提案がありましたし、自分が望んだような素敵なのがあったため。

これだけ沢山の方に提案していただき、ありがとうございました。
良い意味で沢山迷いました。
また何かあった時は、宜しくお願いいたします。

```html
<!DOCTYPE html>
<html lang="ja">
<head>
<meta charset="utf-8">
<title>住所スタンプ 30×80mm</title>
<link rel="stylesheet" href="https://fonts.googleapis.com/css2?family=Noto+Sans+JP:wght@400;500&display=swap">
<style>
  :root {
    --ink: #111111;
    --paper: #ffffff;
    --portrait-light: #ececec;
    --portrait-dark: #9a9a9a;
  }
  html, body {
    margin: 0;
    padding: 0;
    overflow: hidden;
    background: var(--paper);
  }
  .stamp {
    position: relative;
    width: 1200px;
    height: 3152px;
    background: var(--paper);
    color: var(--ink);
    font-family: "Noto Sans JP", sans-serif;
    overflow: hidden;
  }
  .postal-code {
    position: absolute;
    left: 20px;
    top: -6px;
    margin: 0;
    font-size: 150px;
    font-weight: 400;
    letter-spacing: 2px;
    line-height: 1.1;
    white-space: nowrap;
  }
  .vertical {
    position: absolute;
    margin: 0;
    writing-mode: vertical-rl;
    text-orientation: upright;
    line-height: 1;
    white-space: nowrap;
  }
  .person-name {
    left: 40px;
    top: 220px;
    font-size: 300px;
    font-weight: 500;
    letter-spacing: -2px;
  }
  .job-title {
    left: 408px;
    top: 220px;
    font-size: 144px;
    font-weight: 400;
  }
  .company-name {
    left: 676px;
    top: 184px;
    font-size: 188px;
    font-weight: 400;
    letter-spacing: -1px;
  }
  .address {
    left: 984px;
    top: 180px;
    font-size: 176px;
    font-weight: 400;
    letter-spacing: -20px;
  }
  .address .gap { letter-spacing: -100px; }
  .divider {
    position: absolute;
    width: 0;
    border-left: 10px dotted var(--ink);
  }
  .divider--name { left: 614px; top: 220px; height: 1500px; }
  .divider--address { left: 924px; top: 180px; height: 2780px; }
  .portrait {
    position: absolute;
    left: 180px;
    top: 1760px;
    width: 740px;
    height: 1392px;
    background: linear-gradient(180deg, var(--portrait-light) 0%, var(--portrait-dark) 100%);
  }
</style>
</head>
<body>
  <main class="stamp">
    <p class="postal-code">〒000-0000</p>

    <h1 class="vertical person-name">山田太郎</h1>
    <p class="vertical job-title">代表取締役</p>

    <div class="divider divider--name"></div>

    <p class="vertical company-name">株式会社○○○○</p>

    <div class="divider divider--address"></div>

    <p class="vertical address">○○県○○市○○○○○○○<span class="gap">　</span>○-○-○</p>

    <div class="portrait" role="img" aria-label="スーツ姿で拳を握る代表者の似顔絵イラスト"></div>
  </main>
</body>
</html>
```